Business card required for IT Consultancy Business - Tealbrook Consulting.
Company provides the whole nine yards of services across IT Architecture, design and execution.
Basically we provide consulting services to help businesses make sure their technology is enabling their business strategy.
Design for front and back required.
We would like the front of the card to inlcude:
Name
Title
Mobile number
email address
www.tbkc.com.au
Company logos attached.
Thank you
Industry/Entity Type
Business
Contact Information for Business Card
Name
Title
Mobile number
email address
www.tbkc.com.au
Look and feel
Each slider illustrates characteristics of the customer's brand and the style your logo design should communicate.

```html
<!DOCTYPE html>
<html lang="en">
<head>
<meta charset="utf-8">
<title>Tealbrook Consulting – Business Card</title>
<link href="https://fonts.googleapis.com/css2?family=Arimo:wght@400;700&display=swap" rel="stylesheet">
<style>
  :root {
    --page-bg: #ffffff;
    --card-black: #000000;
    --card-glow: #1a1a1a;
    --accent-red: #ea3d1c;
    --brand-blue: #3a86f0;
  }
  html, body {
    margin: 0;
    padding: 0;
    width: 1200px;
    height: 1200px;
    overflow: hidden;
    background: var(--page-bg);
    font-family: "Arimo", Arial, sans-serif;
  }
  .canvas {
    position: relative;
    width: 1200px;
    height: 1200px;
  }
  .card {
    position: absolute;
    left: 246px;
    width: 700px;
    height: 400px;
    background: radial-gradient(ellipse 60% 55% at 50% 0%, var(--card-glow), var(--card-black) 80%);
    overflow: hidden;
  }
  .card--front { top: 157px; }
  .card--back { top: 637px; }

  .brand {
    position: absolute;
    display: flex;
    align-items: center;
    gap: 12px;
  }
  .brand__dot {
    width: 40px;
    height: 40px;
    border-radius: 50%;
    background: var(--accent-red);
    flex: none;
  }
  .brand__name {
    color: var(--brand-blue);
    font-weight: 700;
    font-size: 25px;
    line-height: 1.1;
    letter-spacing: 0.5px;
  }
  .card--front .brand { left: 77px; top: 150px; }
  .card--back .brand { left: 211px; top: 166px; }

  .divider {
    position: absolute;
    left: 359px;
    top: 78px;
    width: 3px;
    height: 243px;
    background: var(--accent-red);
  }
  .contact {
    position: absolute;
    left: 408px;
    top: 98px;
    margin: 0;
    color: var(--brand-blue);
    font-size: 20px;
    line-height: 25px;
  }
  .website {
    position: absolute;
    left: 410px;
    top: 261px;
    color: var(--brand-blue);
    font-size: 20px;
  }
  .rule {
    position: absolute;
    top: 189px;
    height: 3px;
    background: var(--accent-red);
  }
  .rule--left { left: 0; width: 182px; }
  .rule--right { left: 486px; width: 214px; }
</style>
</head>
<body>
<main class="canvas">
  <section class="card card--front">
    <div class="brand">
      <span class="brand__dot"></span>
      <span class="brand__name">Tealbrook<br>Consulting</span>
    </div>
    <div class="divider"></div>
    <p class="contact">
      Name of you<br>
      Title<br>
      0123456789<br>
      name@tbkc.com.au
    </p>
    <div class="website">www.tbkc.com.au</div>
  </section>

  <section class="card card--back">
    <div class="rule rule--left"></div>
    <div class="brand">
      <span class="brand__dot"></span>
      <span class="brand__name">Tealbrook<br>Consulting</span>
    </div>
    <div class="rule rule--right"></div>
  </section>
</main>
</body>
</html>
```